Innovative and exciting banner advert for real estate
Lots of freedom of design
#10 I like the way the 'save thousands in commission' is done with mixed size font. The 'save thousands' stands out very clearly which is important to us
Thanks.
Hi and thank you designers for your attention to our project, there are some great ideas coming in now.
A slight change to the brief:
In the blue screen, please remove 'money back guarantee' and replace with 'no hidden charges' from the green screen so each screen has only 3 bullet points.
Thanks
RPellow
Hi Designers
Please note, we do not require the logo in the adverts just the use of the logo colours as the base.
It is more important that the first line of text stands out. If you are going to insert the logo, please make it a minor element or as #4 has cleverly used it for the bullet points.
Thanks designers for your time and great ideas. #4 I like the way you have used the logo symbol in the bullet points, and that you have aligned the bullets points to the left, it looks good.
#5 the way that 'save thousands' and 'get the best price' stand out clearly is great, this is the message that we are trying to pass on to viewers, it is most important.
If there is any information you need please contact me directly, I will check messages.
Just to clarify, we do not require the logo in the adverts just the use of the logo colours as the base. These adverts are going to be used on our own site.
Regards
Thanks Hostmod for making that clear for designers.
Designers, we don't have images of the product we sell as we provide real estate services (not goods). If looking for inspiration for imagery, residential property is more appropriate than commercial property.
Thanks everyone.
Attention Designers!
PH is looking for static banner design which includes two individual advert frames.
Banner size : 450 wide x 225 high
I'm clarifying with our site technicians exactly what the frames should be.
We originally wanted two individual advert frames, 450 wide x 225 high, with no animation in the frames themselves. However, when trying to work within the Tandelvox fields, we couldn't elect the specific size we required and instead had to opt for a package deal.
I will upload a link to the real estate website template we will be using, the template has 'featured property' images in the centre of the homepage which we will be replacing with our two adverts. That is, we will not have the featured property on the home page at all.
http://skins.brovellanstudio.example/?theme=realestate2
Dear PH,
Is this animated gifs or flash?

```html
<!DOCTYPE html>
<html lang="en">
<head>
<meta charset="utf-8">
<title>Keyhaven Property – Save Thousands in Commission</title>
<link rel="stylesheet" href="https://fonts.googleapis.com/css2?family=Arimo:wght@400;700&display=swap">
<style>
  :root {
    --white: #ffffff;
    --brand-blue: #2a78c0;
    --band-light: #86c0ea;
    --band-mid: #3d8fd0;
    --band-deep: #1563aa;
    --bullet-fill: #cfe3f5;
    --bullet-edge: #9cc4e6;
    --art-light: #dbe9f6;
    --art-mid: #5b9ad6;
  }
  html, body {
    margin: 0;
    padding: 0;
    overflow: hidden;
    background: var(--white);
  }
  .banner {
    position: relative;
    width: 1200px;
    height: 600px;
    overflow: hidden;
    background: var(--white);
    font-family: "Arimo", Arial, sans-serif;
  }
  .brand {
    position: absolute;
    left: 40px;
    top: 100px;
    display: flex;
    align-items: center;
    gap: 16px;
  }
  .brand-square {
    width: 54px;
    height: 54px;
    background: var(--brand-blue);
    border-radius: 6px;
  }
  .brand-name {
    margin: 0;
    font-size: 40px;
    font-weight: 400;
    color: var(--brand-blue);
    letter-spacing: 1px;
    line-height: 1;
  }
  .house-art {
    position: absolute;
    left: 790px;
    top: 14px;
    width: 390px;
    height: 300px;
    border-radius: 18px;
    background: radial-gradient(ellipse at 50% 45%, var(--art-mid) 0%, var(--art-light) 70%, var(--white) 100%);
  }
  .band {
    position: absolute;
    left: 0;
    top: 0;
    width: 1200px;
    height: 600px;
  }
  .headline {
    position: absolute;
    left: 50px;
    top: 300px;
    margin: 0;
    font-weight: 400;
    color: var(--white);
    line-height: 1;
    white-space: nowrap;
  }
  .headline-key {
    font-size: 62px;
    font-weight: 700;
  }
  .headline-rest {
    font-size: 44px;
  }
  .benefits {
    position: absolute;
    left: 50px;
    top: 395px;
    margin: 0;
    padding: 0;
    list-style: none;
  }
  .benefits li {
    display: flex;
    align-items: center;
    gap: 18px;
    height: 66px;
    font-size: 37px;
    color: var(--white);
  }
  .benefits li::before {
    content: "";
    flex: none;
    width: 36px;
    height: 36px;
    background: var(--bullet-fill);
    border: 2px solid var(--bullet-edge);
    box-sizing: border-box;
  }
</style>
</head>
<body>
<main class="banner">
  <div class="brand">
    <div class="brand-square"></div>
    <p class="brand-name">Keyhaven Property</p>
  </div>

  <div class="house-art" role="img" aria-label="Illustration of a blue two-storey house beside a roll of banknotes"></div>

  <svg class="band" viewBox="0 0 1200 600" aria-hidden="true">
    <defs>
      <linearGradient id="band-fill" x1="0" y1="0" x2="0" y2="1">
        <stop offset="0" stop-color="var(--band-light)"/>
        <stop offset="0.35" stop-color="var(--band-mid)"/>
        <stop offset="1" stop-color="var(--band-deep)"/>
      </linearGradient>
    </defs>
    <path d="M0,248 C320,272 760,262 1200,196 L1200,600 L0,600 Z" fill="url(#band-fill)"/>
    <path d="M0,262 C340,290 780,278 1200,214" fill="none" stroke="#ffffff" stroke-opacity="0.35" stroke-width="6"/>
  </svg>

  <h1 class="headline"><span class="headline-key">Save Thousands</span> <span class="headline-rest">in Commission</span></h1>
  <ul class="benefits">
    <li>Private property sales solutions</li>
    <li>Assisted property sales expertise</li>
    <li>No Hidden Charges</li>
  </ul>
</main>
</body>
</html>
```